Farm product labels

This is meant to design a set of labels for the following products:
Sachets (similar to Brindlecombe’s ketchup):
- Size: W4xH9 cm. This is the internal area (inside the four sealing borders) of sachets. Front side contains the design, and back side just texts with the ingredients, nutrition facts and origin. Please check check the attached pictures related to sachet designs for your reference!
- Products:
o Ketchup
o Honey
o Dulcevara (chocolate spread made of cacao, peanuts, and milk)
o Peanut butter
o Fruit jam (either Mango, Guava or Passion fruit)

Stickers (to be added on transparent bags):
- Size: W8xH14 cm. It does not need to be rectangular
- It needs to accommodate small texts with the ingredients, nutrition facts and origin
- Products:
o Tomato paste
o Fruit pulp (either Mango, Guava or Passion fruit)
o Processed vegetables (either Yuca or Sweet potato). They are peeled, chopped, pre-boiled and frozen.

For those interested I’ll provide detailed info as required

Target Market(s)

Hotels. The sachets are specially for breakfast

Requirements
Must have
• All product label designs should:
- Show a similar look, reflecting a single source/branding
- Be attractive and be easy to recognize each product
- Contain the logo of our farm (uploaded)

```html
<!DOCTYPE html>
<html lang="en">
<head>
<meta charset="utf-8">
<title>Farm Product Labels</title>
<link rel="stylesheet" href="https://fonts.googleapis.com/css2?family=Roboto+Condensed:wght@400;700&display=swap">
<style>
  :root{
    --jam-top:#ffc20e;
    --jam-bottom:#4bb748;
    --ketchup-red:#ec1c24;
    --brand-blue:#233f94;
    --title-red:#e0202a;
    --ink:#111111;
    --paper:#ffffff;
    --canvas:#ffffff;
  }
  *{box-sizing:border-box;margin:0;padding:0}
  html,body{width:1200px;height:1200px;overflow:hidden;background:var(--canvas)}
  body{position:relative;font-family:"Roboto Condensed",Arial,sans-serif}

  .label{position:absolute;top:117px;width:214px;height:518px;overflow:hidden;box-shadow:0 6px 14px rgba(0,0,0,.28)}
  .label--jam{background:linear-gradient(180deg,var(--jam-top) 0%,#d7c01f 45%,var(--jam-bottom) 100%)}
  .label--ketchup{background:var(--ketchup-red)}
  .label--jam-back{left:33px}
  .label--jam-front{left:320px}
  .label--ketchup-back{left:653px}
  .label--ketchup-front{left:940px}

  .nutrition-panel{position:absolute;left:30px;top:0;width:154px;height:210px;background:var(--paper);border-radius:0 0 77px 77px / 0 0 34px 34px;padding:12px 10px 0}
  .nutrition-facts{border:1px solid var(--ink);padding:2px 3px;font-family:Arial,sans-serif;font-size:6.4px;color:var(--ink);line-height:1.25}
  .nutrition-facts h3{font-size:10px;font-weight:700;line-height:1}
  .nutrition-facts .serving{border-bottom:3px solid var(--ink);padding-bottom:1px}
  .nutrition-facts .row{display:flex;justify-content:space-between;border-bottom:.6px solid var(--ink)}
  .nutrition-facts .row.sub{padding-left:6px;border-bottom:none}
  .nutrition-facts .row.thick{border-bottom:2px solid var(--ink)}
  .nutrition-facts .row.cal{font-size:7.4px;font-weight:700}
  .nutrition-facts .dv{font-size:4.6px;font-weight:400}
  .nutrition-facts b{font-weight:700}
  .nutrition-facts .foot{font-size:4.6px;padding-top:1px}

  .ingredients{position:absolute;left:14px;right:14px;top:241px;text-align:center;font-family:Arial,sans-serif;font-weight:700;font-size:8.4px;line-height:1.3;color:var(--ink)}
  .ingredients strong{display:block}

  .brand-mark{position:absolute;left:50%;top:192px;transform:translate(-50%,-50%);display:flex;align-items:center;gap:6px;white-space:nowrap;color:var(--brand-blue);font-weight:700;font-size:21px;line-height:1}
  .brand-mark .dot{width:12px;height:12px;border-radius:50%;background:currentColor;flex:none}
  .brand-mark--light{color:var(--paper)}

  .product-badge{position:absolute;left:0;top:327px;width:214px;height:191px}
  .badge-shape{fill:var(--paper);stroke:var(--brand-blue);stroke-width:3}
  .badge-title{font-family:"Roboto Condensed",Arial,sans-serif;font-size:33px;fill:var(--title-red);text-anchor:middle}
  .badge-tagline{font-family:"Roboto Condensed",Arial,sans-serif;font-size:15.5px;fill:var(--brand-blue);text-anchor:middle}

  .sachet{position:absolute;left:211px;top:767px;width:782px;height:340px;border-radius:28px;overflow:hidden;background:linear-gradient(180deg,#d9161e 0%,var(--ketchup-red) 40%,#d51920 100%)}
  .sachet .brand-mark{left:189px;top:170px;font-size:30px}
  .sachet .brand-mark .dot{width:16px;height:16px}
  .sachet .product-badge{left:476px;top:0;width:306px;height:340px}
</style>
</head>
<body>

<svg width="0" height="0" style="position:absolute" aria-hidden="true">
  <defs>
    <radialGradient id="mango-tone" cx="45%" cy="40%" r="60%">
      <stop offset="0" stop-color="#ffd23a"/><stop offset=".6" stop-color="#f39a1e"/><stop offset="1" stop-color="#e0701b"/>
    </radialGradient>
    <radialGradient id="tomato-tone" cx="40%" cy="35%" r="65%">
      <stop offset="0" stop-color="#f26a4f"/><stop offset=".6" stop-color="#d8261c"/><stop offset="1" stop-color="#9e1410"/>
    </radialGradient>
  </defs>
</svg>

<!-- Fruit jam, back -->
<section class="label label--jam label--jam-back">
  <div class="nutrition-panel">
    <div class="nutrition-facts">
      <h3>Nutrition Facts</h3>
      <div class="serving">Per 6 chocolates (70 g)</div>
      <div class="row cal thick"><span>Calories 250</span><span class="dv">% Daily Value*</span></div>
      <div class="row sub"><span><b>Fat</b> 11 g</span><span>15 %</span></div>
      <div class="row sub"><span>Saturated 2.5 g</span><span></span></div>
      <div class="row"><span>&nbsp;+ Trans 0 g</span><span>13 %</span></div>
      <div class="row sub"><span><b>Carbohydrate</b> 40 g</span><span></span></div>
      <div class="row sub"><span>Fibre 6 g</span><span>21 %</span></div>
      <div class="row"><span>Sugars 31 g</span><span>31 %</span></div>
      <div class="row"><span><b>Protein</b> 5 g</span><span></span></div>
      <div class="row thick"><span><b>Cholesterol</b> 0 mg</span><span></span></div>
      <div class="row"><span><b>Sodium</b> 95 mg</span><span>4 %</span></div>
      <div class="row thick"><span>Potassium 450 mg</span><span>10 %</span></div>
      <div class="row"><span>Calcium 75 mg</span><span>6 %</span></div>
      <div class="row thick"><span>Iron 1.50 mg</span><span>8 %</span></div>
      <div class="foot">*5% or less is a <b>little</b>, 15% or more is a <b>lot</b></div>
    </div>
  </div>
  <p class="ingredients"><strong>INGREDIENTS:</strong>DATES, HAZELNUTS, ORGANIC DARK CHOCOLATE* (RAW CANE SUGAR, COCOA MASS, COCOA BUTTER), ORGANIC COCOA POWDER*, VANILLA EXTRACT, SEA SALT.</p>
  <svg class="product-badge" viewBox="0 327 214 191">
    <path class="badge-shape" d="M0 520V482L20 448V415Q20 392 46 388L58 376Q60 340 107 330Q154 340 156 376L168 388Q194 392 194 415V448L214 482V520Z"/>
    <g role="img" aria-label="Mango fruit with a cut slice"><ellipse cx="107" cy="357" rx="22" ry="14" fill="url(#mango-tone)"/></g>
    <text class="badge-title" x="107" y="427">FRUIT JAM</text>
    <text class="badge-tagline" x="107" y="453">My Favourite One</text>
  </svg>
</section>

<!-- Fruit jam, front -->
<section class="label label--jam label--jam-front">
  <div class="brand-mark"><span class="dot"></span><span>Valmora Farms</span></div>
  <svg class="product-badge" viewBox="0 327 214 191">
    <path class="badge-shape" d="M0 520V482L20 448V415Q20 392 46 388L58 376Q60 340 107 330Q154 340 156 376L168 388Q194 392 194 415V448L214 482V520Z"/>
    <g role="img" aria-label="Mango fruit with a cut slice"><ellipse cx="107" cy="357" rx="22" ry="14" fill="url(#mango-tone)"/></g>
    <text class="badge-title" x="107" y="427">FRUIT JAM</text>
    <text class="badge-tagline" x="107" y="453">My Favourite One</text>
  </svg>
</section>

<!-- Ketchup, back -->
<section class="label label--ketchup label--ketchup-back">
  <div class="nutrition-panel">
    <div class="nutrition-facts">
      <h3>Nutrition Facts</h3>
      <div class="serving">Per 6 chocolates (70 g)</div>
      <div class="row cal thick"><span>Calories 250</span><span class="dv">% Daily Value*</span></div>
      <div class="row sub"><span><b>Fat</b> 11 g</span><span>15 %</span></div>
      <div class="row sub"><span>Saturated 2.5 g</span><span></span></div>
      <div class="row"><span>&nbsp;+ Trans 0 g</span><span>13 %</span></div>
      <div class="row sub"><span><b>Carbohydrate</b> 40 g</span><span></span></div>
      <div class="row sub"><span>Fibre 6 g</span><span>21 %</span></div>
      <div class="row"><span>Sugars 31 g</span><span>31 %</span></div>
      <div class="row"><span><b>Protein</b> 5 g</span><span></span></div>
      <div class="row thick"><span><b>Cholesterol</b> 0 mg</span><span></span></div>
      <div class="row"><span><b>Sodium</b> 95 mg</span><span>4 %</span></div>
      <div class="row thick"><span>Potassium 450 mg</span><span>10 %</span></div>
      <div class="row"><span>Calcium 75 mg</span><span>6 %</span></div>
      <div class="row thick"><span>Iron 1.50 mg</span><span>8 %</span></div>
      <div class="foot">*5% or less is a <b>little</b>, 15% or more is a <b>lot</b></div>
    </div>
  </div>
  <p class="ingredients"><strong>INGREDIENTS:</strong>DATES, HAZELNUTS, ORGANIC DARK CHOCOLATE* (RAW CANE SUGAR, COCOA MASS, COCOA BUTTER), ORGANIC COCOA POWDER*, VANILLA EXTRACT, SEA SALT.</p>
  <svg class="product-badge" viewBox="0 327 214 191">
    <path class="badge-shape" d="M0 520V482L20 448V415Q20 392 46 388L58 376Q60 340 107 330Q154 340 156 376L168 388Q194 392 194 415V448L214 482V520Z"/>
    <g role="img" aria-label="Ripe red tomato"><circle cx="107" cy="358" r="15" fill="url(#tomato-tone)"/></g>
    <text class="badge-title" x="107" y="427">KETCHUP</text>
    <text class="badge-tagline" x="107" y="453">My Favourite One</text>
  </svg>
</section>

<!-- Ketchup, front -->
<section class="label label--ketchup label--ketchup-front">
  <div class="brand-mark brand-mark--light"><span class="dot"></span><span>Valmora Farms</span></div>
  <svg class="product-badge" viewBox="0 327 214 191">
    <path class="badge-shape" d="M0 520V482L20 448V415Q20 392 46 388L58 376Q60 340 107 330Q154 340 156 376L168 388Q194 392 194 415V448L214 482V520Z"/>
    <g role="img" aria-label="Ripe red tomato"><circle cx="107" cy="358" r="15" fill="url(#tomato-tone)"/></g>
    <text class="badge-title" x="107" y="427">KETCHUP</text>
    <text class="badge-tagline" x="107" y="453">My Favourite One</text>
  </svg>
</section>

<!-- Ketchup sachet front -->
<section class="sachet">
  <div class="brand-mark brand-mark--light"><span class="dot"></span><span>Valmora Farms</span></div>
  <svg class="product-badge" viewBox="0 0 191 214" preserveAspectRatio="xMaxYMid meet">
    <g transform="translate(-327 214) rotate(-90)">
      <path class="badge-shape" d="M-2 520V482L20 448V415Q20 392 46 388L58 376Q60 340 107 330Q154 340 156 376L168 388Q194 392 194 415V448L216 482V520Z"/>
      <g role="img" aria-label="Ripe red tomato"><circle cx="107" cy="358" r="15" fill="url(#tomato-tone)"/></g>
      <text class="badge-title" x="107" y="427">KETCHUP</text>
      <text class="badge-tagline" x="107" y="453">My Favourite One</text>
    </g>
  </svg>
</section>

</body>
</html>
```